BrivoMetra. Lantern for the Enterprise Worth. Business card

Professional business card for BrivoMetra (Lantern for the Enterprise Worth)
My rationale: Strategy-> Execution-> Results-> Value that lead to the BrivoMetra name: We put the Lantern for the Enterprise Worth.
We deliver value to our customers helping them at defining a good strategy (cyan arrow). 90% of well formulated strategies fail due to poor execution so we also consider strategical execution very important (green arrow). Due to the execution we obtain the results (blue arrow). Finally, the results provide feedback to redefine strategy, and the new strategy has to be executed and new results obtained providing new feedback and on and on. It's like a wheel that finally, must create corporate value: value for shareholders, staholders, employees, providers...-

Target Market(s)

CEOs and steering comitees , invewrnent funds

Industry/Entity Type

Business Consultant

Contact Information for Business Card

Teodoro Vinschetti
CEO & Founder
teodoro.vinschetti@brivometra-example.com
Mobile: +34 655.802.913
www.brivometra-example.com

Colors

Designer to choose colors to be used in the design.

Requirements
Nice to have
• Nice to hace the words: Strategy, execution, results
• Nice to vave the claim: Lantern for the Enterprise Worth
• The three colors should be shown:
• cyan for STRATEGY
• green for EXECUTION
• blue for RESULTS
Should not have
• Complete black background

```html
<!DOCTYPE html>
<html lang="en">
<head>
<meta charset="utf-8">
<title>BrivoMetra — Business Card</title>
<link rel="stylesheet" href="https://fonts.googleapis.com/css2?family=Roboto+Condensed:wght@400;500;700&display=swap">
<style>
  :root {
    --backdrop: #3f3d3b;
    --card-white: #ffffff;
    --brand-navy: #1f3a93;
    --brand-green: #9ccb3b;
    --brand-cyan: #2aa9e0;
    --brand-blue: #1f5fae;
    --text-dark: #3a3a3a;
    --text-white: #ffffff;
  }
  * { box-sizing: border-box; margin: 0; padding: 0; }
  html, body {
    width: 1200px; height: 900px; overflow: hidden;
    background: var(--backdrop);
    font-family: "Roboto Condensed", "Arial Narrow", sans-serif;
  }
  .card {
    position: absolute; left: 311px; width: 577px; height: 328px;
    box-shadow: 0 6px 14px rgba(0,0,0,0.45);
  }
  .card-front {
    top: 98px;
    background:
      radial-gradient(circle at 0% 100%, var(--brand-green) 0%, rgba(156,203,59,0.6) 22%, rgba(156,203,59,0) 50%),
      linear-gradient(100deg, #7dc47f 0%, #30ace3 42%, #1f7fcb 72%, #24469c 100%);
    color: var(--text-white);
    text-align: center;
  }
  .front-brand {
    position: absolute; left: 0; right: 0; top: 170px;
    font-weight: 700; font-size: 48px; line-height: 1; letter-spacing: 0.5px;
  }
  .front-claim, .front-pillars {
    position: absolute; left: 0; right: 0;
    font-weight: 500; font-size: 16px; letter-spacing: 0.9px; text-transform: uppercase;
  }
  .front-claim { top: 225px; }
  .front-pillars { top: 246px; word-spacing: 2px; }
  .card-back { top: 472px; background: var(--card-white); }
  .back-mark {
    position: absolute; left: 432px; top: 580px;
    width: 34px; height: 34px; border-radius: 50%; background: var(--brand-cyan);
    transform: translate(-311px, -472px);
  }
  .back-brand {
    position: absolute; left: 44px; top: 190px;
    font-weight: 700; font-size: 38px; line-height: 1; color: var(--brand-navy);
  }
  .divider {
    position: absolute; left: 256px; top: 106px; width: 2px; height: 116px;
    background: var(--brand-navy);
  }
  .contact { position: absolute; left: 283px; top: 103px; }
  .contact-name {
    font-weight: 700; font-size: 17px; color: var(--brand-navy); letter-spacing: 0.4px;
    text-transform: uppercase;
  }
  .contact-role { font-size: 12px; color: var(--text-dark); margin-top: 2px; text-transform: uppercase; }
  .contact-list { list-style: none; margin-top: 14px; }
  .contact-list li {
    display: flex; align-items: center; gap: 6px;
    font-size: 14px; color: var(--text-dark); height: 24px;
  }
  .contact-list svg { width: 17px; height: 17px; fill: var(--brand-navy); flex: none; }
</style>
</head>
<body>
  <section class="card card-front">
    <div class="front-brand">BrivoMetra</div>
    <div class="front-claim">Lantern for the Enterprise Worth</div>
    <div class="front-pillars">Strategy &nbsp;|&nbsp; Execution &nbsp;|&nbsp; Results</div>
  </section>

  <section class="card card-back">
    <div class="back-mark"></div>
    <div class="back-brand">BrivoMetra</div>
    <div class="divider"></div>
    <div class="contact">
      <div class="contact-name">Teodoro Vinschetti</div>
      <div class="contact-role">CEO &amp; Founder</div>
      <ul class="contact-list">
        <li>
          <svg viewBox="0 0 16 16" aria-hidden="true"><path d="M4 0h8a1.5 1.5 0 0 1 1.5 1.5v13A1.5 1.5 0 0 1 12 16H4a1.5 1.5 0 0 1-1.5-1.5v-13A1.5 1.5 0 0 1 4 0zm0 2v10.5h8V2zm4 11.2a.9.9 0 1 0 0 1.8.9.9 0 0 0 0-1.8z"/></svg>
          +34 655.802.913
        </li>
        <li>
          <svg viewBox="0 0 16 16" aria-hidden="true"><path d="M0 3h16v1.2L8 9 0 4.2zM0 5.6l8 4.8 8-4.8V13H0z"/></svg>
          teodoro.vinschetti@brivometra-example.com
        </li>
        <li>
          <svg viewBox="0 0 16 16" aria-hidden="true"><path d="M8 0a8 8 0 1 0 0 16A8 8 0 0 0 8 0zm0 1.5c.6 0 1.6 1.6 2 4.5H6c.4-2.9 1.4-4.5 2-4.5zM5.3 2A9 9 0 0 0 4.5 6H1.9A6.5 6.5 0 0 1 5.3 2zm5.4 0a6.5 6.5 0 0 1 3.4 4h-2.6a9 9 0 0 0-.8-4zM1.6 7.5h2.8a12 12 0 0 0 0 1H1.6zm4.3 0h4.2a12 12 0 0 1 0 1H5.9zm5.7 0h2.8v1h-2.8a12 12 0 0 0 0-1zM1.9 10h2.6a9 9 0 0 0 .8 4 6.5 6.5 0 0 1-3.4-4zm4.1 0h4c-.4 2.9-1.4 4.5-2 4.5s-1.6-1.6-2-4.5zm5.5 0h2.6a6.5 6.5 0 0 1-3.4 4 9 9 0 0 0 .8-4z"/></svg>
          www.brivometra-example.com
        </li>
      </ul>
    </div>
  </section>
</body>
</html>
```